Harbinger Slabworks, Inc. Business Card

Create a business card that is eye catching and based around concrete sawcutting. I've attached our current business card and logo for reference. We like aspects of the current business card, but it is starting to feel very loud and lost. We would like something that is still fun but is more modern and streamlined.

```html
<!DOCTYPE html>
<html lang="en">
<head>
<meta charset="utf-8">
<title>Harbinger Slabworks, Inc. Business Card</title>
<link href="https://fonts.googleapis.com/css2?family=Oswald:wght@400;500&display=swap" rel="stylesheet">
<style>
  :root {
    --page: #ffffff;
    --card: #161616;
    --card-light: #262626;
    --ink: #ffffff;
    --accent: #c8102e;
    --mark: #2a2a2a;
  }
  * { margin: 0; padding: 0; box-sizing: border-box; }
  html, body { width: 1200px; height: 1000px; overflow: hidden; background: var(--page); }
  .canvas { position: relative; width: 1200px; height: 1000px; }
  .card {
    position: absolute; top: 133px; width: 418px; height: 732px;
    background: radial-gradient(ellipse at 40% 40%, var(--card-light), var(--card) 75%);
    color: var(--ink);
    font-family: "Oswald", sans-serif;
    text-align: center;
  }
  .card--front { left: 140px; }
  .card--back { left: 640px; }
  .brand {
    position: absolute; left: 39px; width: 340px; height: 340px;
    display: flex; flex-direction: column; align-items: center; justify-content: center; gap: 14px;
  }
  .card--front .brand { top: 108px; }
  .card--back .brand { top: 40px; }
  .brand__dot { width: 22px; height: 22px; border-radius: 50%; background: var(--accent); }
  .brand__name {
    font-weight: 500; font-size: 40px; line-height: 1.15; letter-spacing: 3px;
    text-transform: uppercase; color: var(--ink);
  }
  .hotline {
    position: absolute; top: 36px; left: 0; right: 0;
    font-weight: 500; font-size: 48px; letter-spacing: 6px;
  }
  .sep { color: var(--accent); }
  .services { position: absolute; top: 476px; left: 0; right: 0; list-style: none; }
  .services li { font-size: 36px; line-height: 55px; letter-spacing: 1px; }
  .services li::before, .services li::after { content: "·"; color: var(--accent); margin: 0 12px; }
  .contact { position: absolute; top: 398px; left: 0; right: 0; }
  .contact__name { font-weight: 500; font-size: 52px; letter-spacing: 5px; line-height: 64px; }
  .contact__phone { font-size: 36px; letter-spacing: 2px; line-height: 48px; }
  .contact__label { color: var(--accent); }
  .contact__email { font-size: 27px; line-height: 36px; margin-top: 8px; }
  .contact__address { font-size: 27px; line-height: 34px; }
</style>
</head>
<body>
<main class="canvas">
  <section class="card card--front">
    <p class="hotline">855<span class="sep">·</span>SLABCUT</p>
    <div class="brand" role="img" aria-label="Harbinger Slabworks company name">
      <span class="brand__dot"></span>
      <span class="brand__name">Harbinger<br>Slabworks</span>
    </div>
    <ul class="services">
      <li>Wall Sawing</li>
      <li>Core Drilling</li>
      <li>Slab Sawing</li>
      <li>Breaking &amp; Removal</li>
    </ul>
  </section>

  <section class="card card--back">
    <div class="brand" role="img" aria-label="Harbinger Slabworks company name">
      <span class="brand__dot"></span>
      <span class="brand__name">Harbinger<br>Slabworks</span>
    </div>
    <div class="contact">
      <h1 class="contact__name">MARISA DELGADO</h1>
      <p class="contact__phone"><span class="contact__label">OFFICE:</span> 855<span class="sep">·</span>555<span class="sep">·</span>0142</p>
      <p class="contact__phone"><span class="contact__label">CELL:</span> 973<span class="sep">·</span>555<span class="sep">·</span>0178</p>
      <p class="contact__email">Marisa<span class="sep">@</span>HarbingerSlabworks<span class="sep">.</span>com</p>
      <p class="contact__address">48 N<span class="sep">.</span> Alder Ave<span class="sep">.</span></p>
      <p class="contact__address">Ridgefield<span class="sep">,</span> NJ 07657</p>
    </div>
  </section>
</main>
</body>
</html>
```